Modern Dry eye Poster for eye center, Optometrist office

We need a banner to connect to patient about dry eye and treatment. Ask if patient has dry eyes and we offer treatment .
What is dry eye?
Are you suffering for dry, gritty, painful eyes, blurred vision, redness..

Now there is a quick, comfortable and affordable procedure offering relief tofdry eye.

Schedule your dry eye treatment today.

Target Market(s)

Dry eye patient

Font styles to use
Sans Serif

Colors
00a990
ffffff
0492cd
fbf289
85cae6

Requirements
Must have
• Modern design, dry eye patient
Nice to have
• real life model of nice eyes
Should not have
• No cartoon,

```html
<!DOCTYPE html>
<html lang="en">
<head>
<meta charset="utf-8">
<title>What is Dry Eye? – Clearview Optical Rooms</title>
<link href="https://fonts.googleapis.com/css2?family=Montserrat:ital,wght@0,800;0,900;1,800&family=Oswald:wght@600;700&family=Open+Sans:ital,wght@0,400;1,400;1,700;1,800&display=swap" rel="stylesheet">
<style>
  :root {
    --teal: #00a990;
    --blue: #0492cd;
    --sky: #85cae6;
    --yellow: #dcd21c;
    --yellow-soft: #fbf289;
    --ink: #1e2a32;
    --text: #33393d;
    --white: #ffffff;
  }
  * { margin: 0; padding: 0; box-sizing: border-box; }
  html, body { width: 849px; height: 1200px; overflow: hidden; background: var(--white); }
  .poster {
    position: relative;
    width: 849px;
    height: 1200px;
    overflow: hidden;
    background: var(--white);
    font-family: "Open Sans", sans-serif;
    color: var(--text);
  }
  .hero-photo {
    position: absolute;
    left: 0; top: 0;
    width: 849px; height: 600px;
    background:
      radial-gradient(ellipse 260px 200px at 92% 8%, rgba(255,255,255,0.95) 0%, rgba(255,255,255,0) 100%),
      radial-gradient(ellipse 380px 260px at 48% 52%, rgba(244,196,176,0.85) 0%, rgba(244,196,176,0) 100%),
      linear-gradient(180deg,
        #c9937e 0%,
        #d9a994 14%,
        #b57f6c 26%,
        #e2b4a0 38%,
        #edc5b3 55%,
        #e0ad98 72%,
        #d39c86 100%);
  }
  .swoosh { position: absolute; left: 0; top: 360px; width: 849px; height: 260px; }
  .brand {
    position: absolute;
    left: 16px; top: 16px;
    display: flex; align-items: center; gap: 10px;
  }
  .brand-mark { width: 34px; height: 34px; background: var(--yellow-soft); }
  .brand-name {
    font-family: "Montserrat", sans-serif;
    font-weight: 800;
    font-size: 15px;
    color: var(--white);
    letter-spacing: 0.5px;
  }
  .headline {
    position: absolute;
    right: 66px; top: 588px;
    text-align: right;
    font-family: "Montserrat", sans-serif;
  }
  .headline-lead {
    font-style: italic;
    font-weight: 800;
    font-size: 46px;
    color: var(--ink);
    line-height: 1;
  }
  .headline-main {
    font-weight: 900;
    font-size: 84px;
    color: var(--yellow);
    line-height: 1;
    margin-top: 6px;
    letter-spacing: 1px;
  }
  .headline-bar {
    position: absolute;
    right: 14px; top: 596px;
    width: 22px; height: 138px;
    background: var(--teal);
  }
  .symptoms {
    position: absolute;
    left: 36px; top: 748px;
  }
  .symptoms-title {
    font-family: "Oswald", sans-serif;
    font-weight: 700;
    font-size: 44px;
    color: var(--ink);
    line-height: 1.1;
    margin-bottom: 14px;
  }
  .symptom-list { list-style: none; }
  .symptom-list li {
    position: relative;
    padding-left: 26px;
    font-family: "Oswald", sans-serif;
    font-weight: 600;
    font-size: 25px;
    line-height: 38px;
    color: var(--text);
  }
  .symptom-list li::before {
    content: "";
    position: absolute;
    left: 4px; top: 15px;
    width: 9px; height: 9px;
    border-radius: 50%;
    background: var(--ink);
  }
  .device-photo {
    position: absolute;
    left: 500px; top: 730px;
    width: 349px; height: 300px;
    background:
      radial-gradient(ellipse 140px 110px at 72% 60%, rgba(120,140,152,0.55) 0%, rgba(120,140,152,0) 100%),
      linear-gradient(160deg, #ffffff 0%, #e9f1f6 40%, #cddbe4 75%, #aebfca 100%);
  }
  .offer {
    position: absolute;
    left: 36px; top: 1088px;
    width: 790px;
    font-style: italic;
    font-size: 16px;
    line-height: 22px;
    color: var(--text);
  }
  .cta {
    position: absolute;
    left: 36px; top: 1160px;
    font-style: italic;
    font-weight: 800;
    font-size: 17px;
    letter-spacing: 0.4px;
    color: var(--ink);
    text-transform: uppercase;
  }
</style>
</head>
<body>
  <main class="poster">
    <div class="hero-photo" role="img" aria-label="Close-up photo of a woman rubbing a red, irritated dry eye"></div>

    <svg class="swoosh" viewBox="0 0 849 260" aria-hidden="true">
      <path d="M0 175 C 250 60, 560 10, 849 22 L849 260 L0 260 Z" fill="var(--teal)"/>
      <path d="M0 205 C 260 95, 560 50, 849 62 L849 260 L0 260 Z" fill="var(--white)"/>
    </svg>

    <div class="brand">
      <span class="brand-mark"></span>
      <span class="brand-name">CLEARVIEW OPTICAL</span>
    </div>

    <h1 class="headline">
      <div class="headline-lead">What is</div>
      <div class="headline-main">DRY EYE?</div>
    </h1>
    <div class="headline-bar"></div>

    <section class="symptoms">
      <h2 class="symptoms-title">Do you suffer with:</h2>
      <ul class="symptom-list">
        <li>Dry, Gritty, Sandy Sensation</li>
        <li>Irritated Red Eyes</li>
        <li>Burning or Stinging</li>
        <li>Blurred Vision</li>
        <li>Tender Eyelids or</li>
        <li>Watery Eyes</li>
      </ul>
    </section>

    <div class="device-photo" role="img" aria-label="Photo of a dry eye treatment device with its control screen"></div>

    <p class="offer">Now there is a quick, comfortable and affordable procedure offering relief to dry eye. Dry Eye Specialist Clearview Optical Rooms are offering a Dry Eye consultation. Assessments and treatment plan offered to help you manage your Dry Eye symptom.</p>

    <p class="cta">Schedule your dry eye treatment today.</p>
  </main>
</body>
</html>
```